Letterhead

We need a professional, compelling letterhead that can be used for print and email stationary. We have the logo and the letterhead styling and colors should blend seamlessly and be complimentary. Looking for something unique and thoughtful.
Updates

Reason: There are good ideas and am requesting changes to some ideas in order to make a final decision. Thank you for for submissions. Also, I have uploaded the ai file. Please use that file. Thank you.

If you cannot see the .ai version of the logo that I have tried to upload, please message me if you want to make changes to your submission or submit new design and I will send that file to you directly. This .ai will need to be used in order to ensure high quality printing. Thank you.

Target Market(s)

Clients. Business partners.

Industry/Entity Type

It Professional

Requirements
Must have
• Our logo incorporated. Also the phrase, or tag line - where progress takes root.
Should not have
• Not boring. Not typical. Not too busy.

```html
<!DOCTYPE html>
<html lang="en">
<head>
<meta charset="utf-8">
<title>Meridian Advisory Group LLC — Letterhead</title>
<link rel="stylesheet" href="https://fonts.googleapis.com/css2?family=EB+Garamond:wght@400&display=swap">
<style>
  :root {
    --backdrop: #e9ebee;
    --paper: #ffffff;
    --navy: #0b2f5e;
    --band: #04305f;
    --ink: #1d3557;
  }
  * { margin: 0; padding: 0; box-sizing: border-box; }
  html, body {
    width: 1200px;
    height: 997px;
    overflow: hidden;
    background: var(--backdrop);
    font-family: "EB Garamond", Georgia, serif;
  }
  .letterhead {
    position: absolute;
    left: 228px;
    top: 18px;
    width: 744px;
    height: 960px;
    background: var(--paper);
    box-shadow: 0 2px 10px rgba(0,0,0,0.12);
  }
  .brand {
    position: absolute;
    top: 22px;
    left: 0;
    width: 100%;
    display: flex;
    flex-direction: column;
    align-items: center;
    color: var(--navy);
  }
  .brand-mark {
    width: 42px;
    height: 42px;
    border-radius: 50%;
    background: var(--navy);
  }
  .brand-name {
    margin-top: 8px;
    font-size: 19px;
    letter-spacing: 5px;
    line-height: 1;
    padding-left: 5px;
  }
  .brand-sub {
    font-size: 15px;
    line-height: 1.1;
  }
  .tagline {
    position: absolute;
    top: 120px;
    width: 100%;
    text-align: center;
    font-size: 27px;
    color: var(--navy);
    line-height: 1;
  }
  .header-rule {
    position: absolute;
    top: 161px;
    left: 0;
    width: 100%;
    height: 2px;
    background: var(--navy);
  }
  .contact {
    position: absolute;
    top: 906px;
    left: 0;
    width: 100%;
    text-align: center;
    font-size: 14px;
    color: var(--ink);
    word-spacing: 1px;
  }
  .contact span + span { margin-left: 18px; }
  .footer-band {
    position: absolute;
    bottom: 0;
    left: 0;
    width: 100%;
    height: 31px;
    background: var(--band);
  }
</style>
</head>
<body>
  <main class="letterhead">
    <header class="brand">
      <div class="brand-mark"></div>
      <div class="brand-name">MERIDIAN</div>
      <div class="brand-sub">Advisory Group LLC</div>
    </header>
    <p class="tagline">where progress takes root</p>
    <div class="header-rule"></div>
    <footer>
      <p class="contact">
        <span>48 Harbor View Lane Oakridge</span>
        <span>Tel: 1+ (555) 014-2000</span>
        <span>Fax: 1+ (555) 014-2200</span>
      </p>
      <div class="footer-band"></div>
    </footer>
  </main>
</body>
</html>
```